Poster for a variety show

This poster is for a one time variety show with a magician, juggler and ventriloquist. This is a family friendly show with a religious message along with the performances. The poster should be very colorful in a vertical 11"x14" size. The name of the show is "Wonderstruck" which should be prominently featured. This is a colorful show business type poster that should convey energy and excitment

Location: Halvern College of Mountain Studies at Pinecrest Ridge, Marrowfield Auditorium
Date: July 31, 2013 at 7:00 pm
Free Admission
Starring: Illusionist Tomas Brevik, World Record Juggler Oscar Pell and Ventriloquist Neil Fosberg

Words or phrases that might be used in the poster: Amazing Illusions, Spectacular Juggling, Family Friendly Comedy, Audience Participation, Spiritually Uplifting Message

Target Market(s)

Families, college students

Industry/Entity Type

Religious

Requirements
Must have
• Must have time, date and location and use the three photos of the performers. Name "Wonderstruck" should be prominently featured.
Should not have
• Do not use the word "magic" or "magical"

```html
<!DOCTYPE html>
<html lang="en">
<head>
<meta charset="utf-8">
<title>Wonderstruck – Variety Show Poster</title>
<link rel="stylesheet" href="https://fonts.googleapis.com/css2?family=Arimo:wght@400;700&family=Didact+Gothic&display=swap">
<style>
  :root {
    --red: #c1272d;
    --red-deep: #8f1a1f;
    --red-dark: #6e1216;
    --beam: #ffffff;
    --ink: #1c1c1c;
    --blue: #1d6fb8;
    --blue-light: #2aa3dc;
    --ghost: rgba(0, 0, 0, 0.06);
    --lamp: #4a4a4a;
    --photo-frame: #ffffff;
  }
  * { margin: 0; padding: 0; box-sizing: border-box; }
  html, body { width: 943px; height: 1200px; overflow: hidden; background: #fff; }

  .poster {
    position: relative;
    width: 943px;
    height: 1200px;
    overflow: hidden;
    background: linear-gradient(160deg, var(--red) 0%, var(--red) 45%, var(--red-deep) 100%);
    font-family: "Didact Gothic", "Arial", sans-serif;
  }
  .layer { position: absolute; inset: 0; }

  .beam {
    clip-path: polygon(137px 143px, 167px 125px, 943px 530px, 943px 1200px, 488px 1200px);
    background: var(--beam);
  }
  .ghost-words { overflow: hidden; }
  .ghost-words span {
    position: absolute;
    font-family: "Arimo", sans-serif;
    font-weight: 700;
    font-size: 104px;
    color: var(--ghost);
    white-space: nowrap;
  }

  .spotlight {
    position: absolute;
    left: 0; top: 0;
    width: 238px; height: 160px;
  }

  .performer-silhouette {
    position: absolute;
    left: 18px; top: 560px;
    width: 440px; height: 640px;
    border-radius: 46% 46% 0 0 / 30% 30% 0 0;
    background: radial-gradient(ellipse at 50% 40%, rgba(110,18,22,0.85) 0%, rgba(110,18,22,0.55) 60%, rgba(110,18,22,0) 100%);
  }

  .title {
    position: absolute;
    left: 30px; top: 205px;
    font-family: "Arimo", sans-serif;
    font-weight: 700;
    font-size: 122px;
    letter-spacing: -2px;
    line-height: 1;
    white-space: nowrap;
    -webkit-text-stroke: 2px var(--ink);
  }
  .title--on-red { color: #fff; }
  .title--on-beam { color: var(--red); }
  .beam-title { clip-path: polygon(137px 143px, 167px 125px, 943px 530px, 943px 1200px, 488px 1200px); }

  .event-info {
    position: absolute;
    left: 208px; top: 380px;
    font-family: "Arimo", sans-serif;
    font-weight: 700;
  }
  .event-date { color: var(--blue); font-size: 31px; }
  .event-venue {
    color: var(--blue-light);
    font-size: 25px;
    line-height: 1.3;
    margin: 14px 0 0 18px;
  }

  .starring {
    position: absolute;
    left: 445px; top: 540px;
    width: 200px;
    text-align: center;
    font-size: 40px;
    color: var(--ink);
    padding-bottom: 6px;
    border-bottom: 1px solid var(--ink);
  }

  .act {
    position: absolute;
    width: 320px;
    left: 385px;
    text-align: center;
    line-height: 1.6;
  }
  .act-role { font-size: 27px; color: var(--ink); }
  .act-name { font-size: 28px; color: var(--red); }
  .act--illusionist { top: 632px; }
  .act--juggler { top: 830px; left: 375px; }
  .act--ventriloquist { top: 1035px; }

  .headshot {
    position: absolute;
    border: 7px solid var(--photo-frame);
    box-shadow: 3px 5px 12px rgba(0,0,0,0.35);
  }
  .headshot--illusionist {
    left: 693px; top: 595px; width: 170px; height: 168px;
    transform: rotate(4deg);
    background: linear-gradient(160deg, #f4f4f4, #d9d4cf);
  }
  .headshot--juggler {
    left: 716px; top: 792px; width: 156px; height: 200px;
    transform: rotate(-4deg);
    background: radial-gradient(ellipse at 50% 45%, #3a5da8 0%, #13224f 70%, #0a1230 100%);
  }
  .headshot--ventriloquist {
    left: 714px; top: 1008px; width: 162px; height: 150px;
    transform: rotate(4deg);
    background: linear-gradient(160deg, #6b1d1f, #2f1414);
  }

  .ticket {
    position: absolute;
    width: 250px; height: 118px;
    background: #fff;
    border-radius: 6px;
    box-shadow: 2px 4px 10px rgba(0,0,0,0.35);
    padding: 12px;
  }
  .ticket-inner {
    width: 100%; height: 100%;
    border: 1.5px solid var(--blue-light);
    display: flex; align-items: center; justify-content: center;
    text-align: center;
    color: var(--blue-light);
    font-size: 31px;
    line-height: 1.1;
  }
  .ticket--back { left: 100px; top: 900px; transform: rotate(17deg); }
  .ticket--front { left: 55px; top: 995px; transform: rotate(-7deg); }
</style>
</head>
<body>
<main class="poster">

  <div class="layer beam">
    <div class="layer ghost-words" aria-hidden="true">
      <span style="left:100px; top:140px;">Wonderstruck</span>
      <span style="left:150px; top:345px;">Wonderstruck</span>
      <span style="left:300px; top:520px;">le Wonderstruck</span>
      <span style="left:230px; top:650px;">derstruck Wond</span>
      <span style="left:330px; top:770px;">Wonderstruck Wo</span>
      <span style="left:380px; top:880px;">Wonderstruck</span>
      <span style="left:440px; top:1010px;">Wonderstruck</span>
      <span style="left:470px; top:1130px;">Wonderstruck</span>
    </div>
  </div>

  <svg class="spotlight" viewBox="0 0 238 160" role="img" aria-label="Stage spotlight lamp shining down">
    <polygon points="0,0 210,0 238,70 150,150 0,150" fill="var(--lamp)"/>
  </svg>

  <div class="performer-silhouette" role="img" aria-label="Silhouette of a juggler holding clubs"></div>

  <h1 class="title title--on-red">Wonderstruck</h1>
  <div class="layer beam-title" aria-hidden="true">
    <div class="title title--on-beam">Wonderstruck</div>
  </div>

  <section class="event-info">
    <p class="event-date">July 31, 2013 at 7:00 pm</p>
    <p class="event-venue">Halvern College of Mountain Studies<br>at Pinecrest Ridge, Marrowfield Auditorium</p>
  </section>

  <h2 class="starring">Starring:</h2>

  <div class="act act--illusionist">
    <p class="act-role">Illusionist</p>
    <p class="act-name">Tomas Brevik</p>
  </div>
  <div class="headshot headshot--illusionist" role="img" aria-label="Photo of illusionist Tomas Brevik with colourful props"></div>

  <div class="act act--juggler">
    <p class="act-role">World Record Juggler</p>
    <p class="act-name">Oscar Pell</p>
  </div>
  <div class="headshot headshot--juggler" role="img" aria-label="Photo of juggler Oscar Pell on a blue stage"></div>

  <div class="act act--ventriloquist">
    <p class="act-role">Ventriloquist</p>
    <p class="act-name">Neil Fosberg</p>
  </div>
  <div class="headshot headshot--ventriloquist" role="img" aria-label="Photo of ventriloquist Neil Fosberg with his puppet"></div>

  <div class="ticket ticket--back" aria-hidden="true"><div class="ticket-inner">Free<br>Admission</div></div>
  <div class="ticket ticket--front"><div class="ticket-inner">Free<br>Admission</div></div>

</main>
</body>
</html>
```